Legal Agribusiness Capability Brochure Design

Design A4 sized 6 page Legal Agribusiness Capability Brochure. Design is to be consistent with current marketing materials - logo, letterhead, website and business card to be provided.
Cover page - Firm name and logo, Agribusiness Capability Statement heading with image 1 below
Inside cover page - About Us section with image 2 below then Awards section below image
Inside middle page - Our Expertise with image 3 below
Inside back page - Our Experience with image 4 below
Back page - Senior Lawyers with image 5 below
Outside Middle Back Page - Contact Us with image 6
Updates

To provide more details to designers for brochure

Target Market(s)

Agribusiness - Australia

Industry/Entity Type

Legal

Colors

Designer to choose colors to be used in the design.

Requirements
Must have
• Use content from uloaded file - Agribusiness Brochure Content
• Use images uploaded
• Professional appearance
• Consistent with current marketing and website https://tallowcreeklegal.com.au/

```html
<!DOCTYPE html>
<html lang="en">
<head>
<meta charset="utf-8">
<title>Tallow Creek Legal – Agribusiness Capability Statement</title>
<link href="https://fonts.googleapis.com/css2?family=Hind:wght@400;500;600&family=Signika:wght@600;700&display=swap" rel="stylesheet">
<style>
:root{
  --blue:#1b8ad6;
  --blue-deep:#0f6fb5;
  --ink:#1d1d1f;
  --grey:#6d6f72;
  --paper:#ffffff;
  --paper-edge:#e4e5e7;
  --backdrop:#eceef1;
  --foot:#222326;
  --gold:#d9b35a;
}
*{box-sizing:border-box;margin:0;padding:0}
html,body{width:1200px;height:2414px;overflow:hidden;background:var(--backdrop)}
body{position:relative;font-family:"Hind",Arial,sans-serif;color:var(--ink)}
.spread{position:absolute;left:111px;width:1008px;height:715px;display:flex}
.spread-cover{top:49px}
.spread-inner{top:851px}
.spread-back{top:1649px}
.page{position:relative;width:504px;height:715px;overflow:hidden;background:linear-gradient(90deg,var(--paper) 80%,var(--paper-edge))}
.page.right{background:linear-gradient(90deg,var(--paper-edge),var(--paper) 14%)}
.page-foot{position:absolute;left:0;right:0;bottom:0;height:18px;background:var(--foot);z-index:3}
.photo{position:absolute;z-index:0}
.page > :not(.photo){z-index:2}

/* masthead */
.masthead{position:absolute;left:22px;right:16px;top:46px;height:60px;display:flex;align-items:center;justify-content:space-between}
.brand{display:flex;align-items:center;gap:6px}
.brand-mark{width:42px;height:30px;background:var(--blue);border-radius:4px}
.brand-name{font-family:"Signika",sans-serif;font-weight:600;color:var(--blue);font-size:14px;line-height:14px;text-transform:uppercase}
.badges{display:flex;gap:22px;align-items:center}
.badge{width:58px;height:58px;border-radius:50%;border:2px solid var(--gold);background:#fbf7ec}
.seal{width:64px;height:64px;border-radius:50%;border:2px solid #555;background:#f3f3f3}

/* copy */
.section-title{font-family:"Signika",sans-serif;font-weight:700;color:var(--blue);font-size:19px;text-transform:uppercase;letter-spacing:.2px}
.copy{position:absolute;font-size:8.6px;line-height:1.3}
.copy p{margin-bottom:6px}
.ticks{list-style:none}
.ticks li{position:relative;padding-left:11px;margin-bottom:2px}
.ticks li::before{content:"";position:absolute;left:0;top:2px;width:4px;height:4px;border-right:1.6px solid var(--blue);border-bottom:1.6px solid var(--blue);transform:rotate(-45deg)}
.copy.justify{text-align:justify}

/* cover */
.cover-head{top:76px}
.cover-title{position:absolute;left:38px;top:590px;font-family:"Signika",sans-serif;font-weight:700;color:#fff;font-size:31px;line-height:34px;text-transform:uppercase}

/* contact */
.contact-frame{position:absolute;left:58px;top:284px;width:380px;height:228px;border:2px solid #fff;border-radius:18px}
.contact-title{position:absolute;left:0;width:504px;top:268px;text-align:center;font-family:"Hind",sans-serif;font-weight:500;font-size:28px;color:#fff;line-height:32px}
.contact-title span{background:var(--blue);padding:0 12px}
.office{position:absolute;top:292px;width:170px;text-align:center;color:#fff;font-size:8.6px;line-height:1.15}
.office svg{display:block;margin:0 auto 5px;width:16px;height:16px;fill:#fff}
.office .line{min-height:40px}
.office-a{left:72px}
.office-b{left:282px}
.site{position:absolute;top:490px;width:504px;text-align:center;color:#fff;font-size:10px;font-weight:500}
.backcover-brand{position:absolute;left:0;width:504px;top:622px;display:flex;justify-content:center}
.backcover-brand .brand-mark{width:64px;height:46px}
.backcover-brand .brand-name{font-size:24px;line-height:24px}

/* lawyers */
.portrait{position:absolute;width:118px;height:90px;border:2px solid var(--blue);border-radius:8px;background:linear-gradient(#e9e9e9,#bdbdbd)}
.lawyer-name{position:absolute;font-family:"Signika",sans-serif;font-weight:600;font-size:9px;color:var(--blue);text-transform:uppercase}
.lawyer-name b{color:var(--ink);font-weight:600}
.bio{position:absolute;left:178px;width:300px;font-size:7.4px;line-height:1.2;text-align:justify}
.bio p{margin-bottom:5px}
.bio .ticks li{margin-bottom:1px}
</style>
</head>
<body>

<section class="spread spread-cover">
  <article class="page left back-cover">
    <div class="photo" style="left:0;top:0;width:504px;height:200px;background:linear-gradient(180deg,#8b8478,#c9b48a 55%,#a5843f)" role="img" aria-label="Yellow combine harvester cutting a wheat crop under a cloudy sky"></div>
    <svg class="photo" style="left:0;top:0" width="504" height="715" viewBox="0 0 504 715">
      <defs><linearGradient id="greyfoot" x1="0" x2="1"><stop offset="0" stop-color="#ececec"/><stop offset="1" stop-color="#d4d4d4"/></linearGradient></defs>
      <rect x="0" y="560" width="504" height="140" fill="url(#greyfoot)"/>
      <path d="M0,196 H410 Q500,196 504,150 V520 Q504,590 434,590 H0 Z" fill="#fff"/>
      <path d="M0,200 H410 Q500,200 504,156 V520 Q504,585 434,585 H0 Z" fill="var(--blue)"/>
    </svg>
    <div class="contact-frame"></div>
    <h2 class="contact-title"><span>Contact</span></h2>
    <div class="office office-a">
      <div class="line"><svg viewBox="0 0 24 24"><path d="M12 2a7 7 0 0 0-7 7c0 5 7 13 7 13s7-8 7-13a7 7 0 0 0-7-7zm0 9.5A2.5 2.5 0 1 1 12 6.5a2.5 2.5 0 0 1 0 5z"/></svg>Suite 2, Harbourview House<br>14 Marine Lane<br>Geraldton WA 6530</div>
      <div class="line" style="margin-top:4px"><svg viewBox="0 0 24 24"><path d="M6.6 10.8a15 15 0 0 0 6.6 6.6l2.2-2.2a1 1 0 0 1 1-.25 11.4 11.4 0 0 0 3.6.57 1 1 0 0 1 1 1V20a1 1 0 0 1-1 1A17 17 0 0 1 3 4a1 1 0 0 1 1-1h3.5a1 1 0 0 1 1 1c0 1.25.2 2.45.57 3.57a1 1 0 0 1-.25 1z"/></svg>+61 8 9900 1100</div>
      <div class="line"><svg viewBox="0 0 24 24"><path d="M6 3h12v5H6zM4 9h16a2 2 0 0 1 2 2v6h-4v4H6v-4H2v-6a2 2 0 0 1 2-2zm4 7v3h8v-3z"/></svg>+ 61 8 9900 1199</div>
      <div class="line" style="margin-top:6px"><svg viewBox="0 0 24 24"><path d="M3 5h18v14H3zm2 2v.5l7 5 7-5V7z"/></svg>info@tallowcreeklegal.com.au</div>
    </div>
    <div class="office office-b">
      <div class="line" style="min-height:54px"><svg viewBox="0 0 24 24"><path d="M12 2a7 7 0 0 0-7 7c0 5 7 13 7 13s7-8 7-13a7 7 0 0 0-7-7zm0 9.5A2.5 2.5 0 1 1 12 6.5a2.5 2.5 0 0 1 0 5z"/></svg>88 Kingsway Avenue<br>West Perth WA 6005</div>
      <div class="line" style="margin-top:4px"><svg viewBox="0 0 24 24"><path d="M6.6 10.8a15 15 0 0 0 6.6 6.6l2.2-2.2a1 1 0 0 1 1-.25 11.4 11.4 0 0 0 3.6.57 1 1 0 0 1 1 1V20a1 1 0 0 1-1 1A17 17 0 0 1 3 4a1 1 0 0 1 1-1h3.5a1 1 0 0 1 1 1c0 1.25.2 2.45.57 3.57a1 1 0 0 1-.25 1z"/></svg>+61 8 9300 2200</div>
      <div class="line"><svg viewBox="0 0 24 24"><path d="M6 3h12v5H6zM4 9h16a2 2 0 0 1 2 2v6h-4v4H6v-4H2v-6a2 2 0 0 1 2-2zm4 7v3h8v-3z"/></svg>+ 61 8 9300 2299</div>
      <div class="line" style="margin-top:6px"><svg viewBox="0 0 24 24"><path d="M3 5h18v14H3zm2 2v.5l7 5 7-5V7z"/></svg>info@tallowcreeklegal.com.au</div>
    </div>
    <div class="site">www.tallowcreeklegal.com.au</div>
    <div class="backcover-brand"><div class="brand"><span class="brand-mark"></span><span class="brand-name">Tallow Creek<br>Legal</span></div></div>
    <div class="page-foot"></div>
  </article>

  <article class="page right front-cover" style="background:linear-gradient(180deg,#f4f4f4,#e3e3e3 30%,#f4f4f4)">
    <header class="masthead cover-head">
      <div class="brand"><span class="brand-mark"></span><span class="brand-name">Tallow Creek<br>Legal</span></div>
      <div class="badges"><span class="badge"></span><span class="badge"></span><span class="badge"></span><span class="seal"></span></div>
    </header>
    <div class="photo" style="left:0;top:193px;width:504px;height:360px;border-top-left-radius:70px;background:linear-gradient(180deg,#c9b79a,#d9c39b 40%,#a6845e 70%,#8a5a3a)" role="img" aria-label="Flock of merino sheep standing on a dry red paddock"></div>
    <svg class="photo" style="left:0;top:520px" width="504" height="180" viewBox="0 0 504 180">
      <path d="M0,100 Q0,55 60,55 H504 V180 H0 Z" fill="#fff"/>
      <path d="M4,110 Q4,66 62,66 H504 V180 H4 Z" fill="var(--blue)"/>
    </svg>
    <h1 class="cover-title">Agribusiness Capability<br>Statement</h1>
    <div class="page-foot"></div>
  </article>
</section>

<section class="spread spread-inner">
  <article class="page left">
    <div class="photo" style="left:0;top:520px;width:504px;height:180px;background:linear-gradient(180deg,#8fb3d6,#bcd0e0 18%,#e8e23a 32%,#c9d640 55%,#6f9a3a 80%,#4d6f2c)" role="img" aria-label="Rolling farmland with bright yellow canola fields and green pasture"></div>
    <svg class="photo" style="left:0;top:0" width="504" height="560" viewBox="0 0 504 560">
      <path d="M0,0 H504 V480 Q504,540 440,540 H0 Z" fill="#fff"/>
      <path d="M0,540 H440 Q504,540 504,480 V490 Q504,548 440,548 H0 Z" fill="var(--blue-deep)"/>
    </svg>
    <header class="masthead">
      <div class="brand"><span class="brand-mark"></span><span class="brand-name">Tallow Creek<br>Legal</span></div>
      <div class="badges"><span class="badge"></span><span class="badge"></span><span class="badge"></span><span class="seal"></span></div>
    </header>
    <div class="copy" style="left:36px;top:140px;width:440px">
      <h2 class="section-title" style="margin-left:32px;margin-bottom:8px">About Us</h2>
      <ul class="ticks">
        <li>Independent commercial law firm with offices in Geraldton and Perth</li>
        <li>Senior lawyers offering a combined 65 years of legal experience</li>
        <li>Practical advice in a professional and timely manner</li>
        <li>Client relationships built on trust</li>
        <li>Unfettered access to senior lawyers</li>
        <li>Direct and ongoing partner level involvement for each client</li>
        <li>Utilise the best information technology available to maintain high levels of efficiency and confidentiality.</li>
      </ul>
      <h2 class="section-title" style="margin:8px 0 6px 32px">Agribusiness Legal Awards</h2>
      <ul class="ticks">
        <li>Ranked as a “Leading Agribusiness Law Firm – Western Australia, 2019” (Top 4)</li>
        <li>Ranked as a “Leading Agribusiness Law Firm – Western Australia, 2018” (Top 4)</li>
        <li>Ranked as a “Leading Agribusiness Law Firm – Western Australia, 2017” (Top 5)</li>
      </ul>
      <h2 class="section-title" style="margin:8px 0 10px 34px">Quality Practice Standard</h2>
      <p style="margin-left:-2px">We are part of a select group of law firms which has been awarded the Quality Practice Standard by the Westland Law Council. As a result, we are able to better serve our clients by:</p>
      <ul class="ticks" style="margin-top:10px">
        <li>Adopting modern quality management principles;</li>
        <li>Focusing on clients’ requirements and client care; and</li>
        <li>Striving for consistency of service for all clients by all at the firm.</li>
      </ul>
    </div>
    <div class="page-foot"></div>
  </article>

  <article class="page right">
    <div class="photo" style="left:0;top:430px;width:504px;height:270px;background:linear-gradient(180deg,#6b6659,#9a8a6c 35%,#5b4a37 70%,#2f261d)" role="img" aria-label="Stockman on horseback mustering cattle through dust at dusk"></div>
    <svg class="photo" style="left:0;top:0" width="504" height="560" viewBox="0 0 504 560">
      <path d="M0,0 H504 V540 H70 Q0,540 0,470 Z" fill="#fff"/>
      <path d="M0,470 Q0,540 70,540 H504 V548 H66 Q-4,548 -4,470 Z" fill="var(--blue-deep)"/>
    </svg>
    <header class="masthead">
      <div class="brand"><span class="brand-mark"></span><span class="brand-name">Tallow Creek<br>Legal</span></div>
      <div class="badges"><span class="badge"></span><span class="badge"></span><span class="badge"></span><span class="seal"></span></div>
    </header>
    <div class="copy" style="left:46px;top:140px;width:435px">
      <h2 class="section-title" style="margin-left:32px;margin-bottom:10px">Expertise</h2>
      <p>Over several decades our senior lawyers have advised clients involved in wheat, canola, lupin, wool, beef, dairy, wool, lamb, poultry, piggery, viticulture, forestry and plantation businesses.</p>
      <p>Our senior lawyers have strong family connections with pastoralists which allows them to better appreciate the challenges faced in agribusiness.</p>
      <p>Our family connection with pastoralists and our strong technical expertise in agribusiness law places Tallow Creek Legal in a unique position to advise clients in the agribusiness industry.</p>
      <p>We can assist with the following agribusiness matters:</p>
      <ul class="ticks">
        <li>Agribusiness property contracts, agreements and deeds;</li>
        <li>Sale and purchase of agribusiness and farm assets;</li>
        <li>Pastoral lease advice;</li>
        <li>Native Title advice concerning access and compensation agreements;</li>
        <li>Land access agreements with mining, energy and telecommunications companies;</li>
        <li>Partnership, trust, corporation and joint venture advice;</li>
        <li>Farm Leases, Share Farming Agreements and Livestock Management Agreements;</li>
        <li>Carbon trading advice;</li>
        <li>Mortgages and securities;</li>
        <li>Farm succession planning, including Wills, Enduring Powers of Attorney and Guardianship;</li>
        <li>Employment advice;</li>
        <li>Deceased estates and probate, including advice concerning family provision claims; and</li>
        <li>Disputes.</li>
      </ul>
    </div>
    <div class="page-foot"></div>
  </article>
</section>

<section class="spread spread-back">
  <article class="page left">
    <div class="photo" style="left:0;top:520px;width:504px;height:180px;background:linear-gradient(180deg,#6f7fa6,#e58a5c 35%,#f0a245 55%,#8a3a1e 80%,#3b1d12)" role="img" aria-label="Outback sunset with a windmill silhouetted against an orange sky"></div>
    <svg class="photo" style="left:0;top:0" width="504" height="560" viewBox="0 0 504 560">
      <path d="M0,0 H504 V480 Q504,540 440,540 H0 Z" fill="#fff"/>
      <path d="M0,540 H440 Q504,540 504,480 V490 Q504,548 440,548 H0 Z" fill="var(--blue-deep)"/>
    </svg>
    <header class="masthead">
      <div class="brand"><span class="brand-mark"></span><span class="brand-name">Tallow Creek<br>Legal</span></div>
      <div class="badges"><span class="badge"></span><span class="badge"></span><span class="badge"></span><span class="seal"></span></div>
    </header>
    <div class="copy justify" style="left:30px;top:140px;width:444px;font-size:8px;line-height:1.2">
      <h2 class="section-title" style="margin-left:48px;margin-bottom:8px">Experience</h2>
      <p>Our senior lawyers have accumulated a wealth of experience in agribusiness law.</p>
      <p>Most of our work is subject to confidentiality which prevents us from disclosing any confidential information. However, we are able to disclose that our experience in agribusiness includes:</p>
      <ul class="ticks">
        <li style="margin-bottom:6px">Advising clients with respect to the sale and acquisition of farmland, including due diligence enquiries, preparation and review of contracts for sale, registration of securities and settlement.</li>
        <li style="margin-bottom:6px">Advising farmer in relation to the 180-megawatt Banksia Ridge Wind Farm to be constructed on farmland near Eneabba, with a project value of up to AUD500 million and which is recognised as one of the best renewable projects in Australia.</li>
        <li style="margin-bottom:6px">Advising pastoral lease holders on the sale and purchase of pastoral leases.</li>
        <li style="margin-bottom:6px">Advising client on the termination of a vendor terms agreement for the sale of a farm and the repossession and resale of the farm.</li>
        <li style="margin-bottom:6px">Advising numerous clients on various agreements with mining companies, including Royalty Agreements, Exploration Agreements, Land Access Deeds, Leases, Transmission Line Works Agreements, Deeds of Settlement and Release, Easement Deeds and Lay-Down Area Agreements.</li>
        <li style="margin-bottom:6px">Advising on Access and Compensation Agreements with native title claimants.</li>
        <li style="margin-bottom:6px">Advising client in relation to restructure of farmland and the transfer of the farmland to family members, trusts and a SMSF to qualify for the duties exemption under the Duties Act.</li>
        <li style="margin-bottom:6px">Advising client in relation to the settlement of a farming partnership and trust dispute.</li>
        <li style="margin-bottom:6px">Advising various farming families / corporate groups in relation to the restructuring of farm assets and exempt family farm transactions under the Duties Act.</li>
        <li>Advising farmers in relation to estate disputes and claims, including claims in the Supreme Court under the Family Provision Act.</li>
      </ul>
    </div>
    <div class="page-foot"></div>
  </article>

  <article class="page right">
    <div class="photo" style="left:0;top:540px;width:504px;height:160px;background:linear-gradient(180deg,#b9cde0,#8fae6a 30%,#a4532f 55%,#c79a3e 75%,#7e5a38)" role="img" aria-label="Rows of autumn grapevines in red and gold leading into the distance"></div>
    <svg class="photo" style="left:0;top:0" width="504" height="560" viewBox="0 0 504 560">
      <path d="M0,0 H504 V540 H70 Q0,540 0,470 Z" fill="#fff"/>
      <path d="M0,470 Q0,540 70,540 H504 V548 H66 Q-4,548 -4,470 Z" fill="var(--blue-deep)"/>
    </svg>
    <header class="masthead">
      <div class="brand"><span class="brand-mark"></span><span class="brand-name">Tallow Creek<br>Legal</span></div>
      <div class="badges"><span class="badge"></span><span class="badge"></span><span class="badge"></span><span class="seal"></span></div>
    </header>
    <h2 class="section-title" style="position:absolute;left:78px;top:143px">Senior Lawyers</h2>
    <div class="portrait" style="left:42px;top:180px" role="img" aria-label="Portrait photograph of Sam Corder"></div>
    <div class="lawyer-name" style="left:48px;top:278px">Sam Corder <b>- Principal</b></div>
    <div class="bio" style="top:180px">
      <p>Sam has practised exclusively as a commercial lawyer for over 20 years initially at Perth law firms and since 2009 in Geraldton.</p>
      <p>In 2011, Sam established Tallow Creek Legal in Geraldton and expanded with the opening of a Perth office in 2017.</p>
      <p>Sam has advised on a large number of commercial matters and disputes, particularly in relation to agribusiness, business, property, wills and estates. He has a proven track record of delivering results to clients, especially in relation to more complex commercial transactions and disputes.</p>
      <p>Sam has a specific interest in agribusiness, primarily due to his family being involved in agribusiness for several generations.</p>
      <p>Ranked by Harlow’s Guide as:</p>
      <ul class="ticks" style="margin-left:6px">
        <li>“Preeminent Agribusiness Lawyer - Western Australia, 2019” (Top 2 in W.A.)</li>
        <li>“Leading Agribusiness Lawyer - Western Australia, 2018” (Top 5 in W.A.)</li>
        <li>“Leading Agribusiness Lawyer - Western Australia, 2017” (Top 7 in W.A.)</li>
      </ul>
    </div>
    <div class="portrait" style="left:42px;top:360px" role="img" aria-label="Portrait photograph of Neil Corder"></div>
    <div class="lawyer-name" style="left:38px;top:458px">Neil Corder <b>- Consultant</b></div>
    <div class="bio" style="top:378px">
      <p>Neil was awarded a Bachelor of Laws from the Coastal State University in 1973. Since then Neil has been a partner at firms in Geraldton and Fremantle, as well as a principal of firms in Geraldton and Fremantle. In late 2009 Neil and his wife, Ruth, made the decision to move back to Geraldton where they had previously lived for approximately 11 years.</p>
      <p>Neil has accumulated experience in a wide range of areas in over 45 years of legal practice, particularly in relation to Agribusiness disputes and litigation, which is of great benefit to his clients.</p>
    </div>
    <div class="page-foot"></div>
  </article>
</section>

</body>
</html>
```